Book cover design, title is "Go Solo Now: How to Swap Your Salary in 10 Seasons"

Design a cover for a book about freelancing. Example of my previous book's cover attached. Book title is "Go Solo Now: How to Swap Your Salary in 10 Seasons". Looking to target people who have a 9-5 job but are seeking to try out freelancing as a way to supplement income and eventually quit their day job.

Target Market(s)

Looking to target people who have a 9-5 job but are seeking to try out freelancing as a way to supplement income and eventually quit their day job.

Industry/Entity Type

Consulting

Font styles to use
Serif
Sans Serif

Colors

Designer to choose colors to be used in the design.

Requirements
Must have
• I love these books covers...
• https://www.pagelodge.example/Tame-Notebin-Casual-Sorting-Settled-ebook/dp/Q71MWRTZPA/ref=asap_bc?ie=UTF8
• https://www.pagelodge.example/Bright-Dawn-Scribes-Drafting-Doubles/dp/5830617294/ref=asap_bc?ie=UTF8
• https://www.pagelodge.example/Way-Pen-Factual-eBook-Weeks-ebook/dp/Q93KT41ZXN/ref=asap_bc?ie=UTF8
• https://www.pagelodge.example/Ritual-Piling-Tiny-Shifts-Moments/dp/6027158392/ref=asap_bc?ie=UTF8
• https://www.pagelodge.example/Boost-Each-Hour-Core-ebook/dp/Q82WFN6JTM/ref=asap_bc?ie=UTF8
• https://www.pagelodge.example/Artisan-Co-Total-Thriving-Gig-ebook/dp/Q66813XKVR/ref=sr_1_4?ie=UTF8&qid=2738405519&sr=8-4&keywords=freelancing
Should not have
• Don't submit 3D renderings, just the front cover image please.

```html
<!DOCTYPE html>
<html lang="en">
<head>
<meta charset="utf-8">
<title>Go Solo Now: Book Cover</title>
<link rel="stylesheet" href="https://fonts.googleapis.com/css2?family=Oswald:wght@500;600&family=Archivo:ital,wght@1,800&display=swap">
<style>
  :root {
    --page-bg: #e6e6e6;
    --cover-black: #070707;
    --cover-edge: #161616;
    --title-blue: #2a62a6;
    --subtitle-gold: #d6a21e;
    --photo-dark: #141414;
    --photo-shadow: #232019;
    --photo-denim: #4d6893;
    --photo-denim-deep: #2c3f5e;
    --photo-yellow: #c4a233;
    --photo-yellow-deep: #8a7222;
    --spotlight: rgba(150, 150, 150, 0.32);
  }
  * { margin: 0; padding: 0; box-sizing: border-box; }
  html, body {
    width: 1200px;
    height: 1200px;
    overflow: hidden;
    background: var(--page-bg);
  }
  .canvas {
    width: 1200px;
    height: 1200px;
    display: flex;
    align-items: center;
    justify-content: center;
  }
  .book-cover {
    position: relative;
    width: 780px;
    height: 1140px;
    background: linear-gradient(180deg, var(--cover-edge) 0%, var(--cover-black) 38%);
    overflow: hidden;
  }
  .book-title {
    position: absolute;
    top: 110px;
    left: 0;
    width: 100%;
    text-align: center;
    font-family: "Oswald", "Arial Narrow", sans-serif;
    font-weight: 600;
    font-size: 104px;
    line-height: 1;
    letter-spacing: -1px;
    color: var(--title-blue);
    transform: scaleY(1.25);
    z-index: 2;
  }
  .book-title .initial { font-size: 140px; }
  .book-subtitle {
    position: absolute;
    top: 378px;
    left: 0;
    width: 100%;
    font-family: "Archivo", "Arial Black", sans-serif;
    font-style: italic;
    font-weight: 800;
    font-size: 46px;
    line-height: 1.05;
    color: var(--subtitle-gold);
    letter-spacing: 1px;
    z-index: 2;
  }
  .book-subtitle span { display: block; }
  .book-subtitle .line-one { padding-left: 270px; }
  .book-subtitle .line-two { padding-left: 225px; }
  .book-subtitle .line-three { padding-left: 360px; }

  .cover-photo {
    position: absolute;
    left: 0;
    bottom: 0;
    width: 100%;
    height: 620px;
  }
  .cover-photo svg { display: block; width: 100%; height: 100%; }
</style>
</head>
<body>
<main class="canvas">
  <article class="book-cover">
    <h1 class="book-title"><span class="initial">G</span>o <span class="initial">S</span>olo <span class="initial">N</span>ow</h1>
    <p class="book-subtitle">
      <span class="line-one">How to Swap</span>
      <span class="line-two">Your Salary</span>
      <span class="line-three">in 10 Seasons</span>
    </p>
    <div class="cover-photo" role="img" aria-label="Photo of a young man in glasses and a denim shirt sitting on a yellow sofa, writing in a notebook under a soft spotlight">
      <svg viewBox="0 0 780 620" preserveAspectRatio="none" aria-hidden="true">
        <defs>
          <linearGradient id="photo-base" x1="0" y1="0" x2="0" y2="1">
            <stop offset="0" stop-color="#070707"/>
            <stop offset="0.35" stop-color="#141414"/>
            <stop offset="0.6" stop-color="#232019"/>
            <stop offset="0.72" stop-color="#8a7222"/>
            <stop offset="0.8" stop-color="#c4a233"/>
            <stop offset="1" stop-color="#8a7222"/>
          </linearGradient>
          <radialGradient id="spotlight-glow" cx="0.5" cy="0.45" r="0.5">
            <stop offset="0" stop-color="#8a8a8a" stop-opacity="0.35"/>
            <stop offset="0.75" stop-color="#5a5a5a" stop-opacity="0.22"/>
            <stop offset="1" stop-color="#3a3a3a" stop-opacity="0.1"/>
          </radialGradient>
          <radialGradient id="denim-tone" cx="0.5" cy="0.5" r="0.5">
            <stop offset="0" stop-color="#4d6893"/>
            <stop offset="0.6" stop-color="#2c3f5e" stop-opacity="0.85"/>
            <stop offset="1" stop-color="#2c3f5e" stop-opacity="0"/>
          </radialGradient>
          <linearGradient id="fade-top" x1="0" y1="0" x2="0" y2="1">
            <stop offset="0" stop-color="#070707"/>
            <stop offset="1" stop-color="#070707" stop-opacity="0"/>
          </linearGradient>
        </defs>
        <rect class="photo-base" width="780" height="620" fill="url(#photo-base)"/>
        <circle class="photo-spotlight" cx="520" cy="300" r="230" fill="url(#spotlight-glow)"/>
        <ellipse class="photo-denim-tone" cx="350" cy="440" rx="190" ry="210" fill="url(#denim-tone)"/>
        <rect class="photo-fade" width="780" height="140" fill="url(#fade-top)"/>
      </svg>
    </div>
  </article>
</main>
</body>
</html>
```